Baby Care Print Log for Nannies and Parents- Creating a brand/style I can use across different forms

I am creating a notebook for babysitters to use to communicate with parents about the children they care for. I will be creating many different forms (emergency contacts, daily logs, shopping lists, etc.)
I need a look and feel from which to style these forms from. I am starting by designing the daily baby care log. I need a designer to take my Word doc with just text on it, and create a visual approach to make this visually appealing.
I do not want this to be extremely "babyish" with cartoon styling. I want it to be more of a professional looking style. I would like to be able to color each different document a different color palette, yet keep the similar look and feel. My logo is attached for inspiration. I use real photography across my website plumhollowkit.com.
Updates
I will be re-designing my Wordpress website based on what design I like best and also will need other forms completed once I pick a design. I am hoping to work with someone who I can hire for further development needs as well. Added Saturday, February 11, 2017
Target Market(s)
Professional Parents
Industry/Entity Type
Education
Requirements
Must have
- color, pop, visual appeal
- Please use the color in my logo and any complementary colors that you think work well with it. I definitely like colored patterns, ombre, colored backgrounds, etc. I'd prefer for it not to be completely white with only pops of color here and there.
Nice to have
- My logo somewhere subtly on the form
- Photography elements
Should not have
- cartoon images of babies, etc. I use real photography across my website with the exception of my logo umbrella.

```html
<!DOCTYPE html>
<html lang="en">
<head>
<meta charset="utf-8">
<title>Plum Hollow Kit – Daily Care Log</title>
<link href="https://fonts.googleapis.com/css2?family=Quicksand:wght@400;500;600;700&display=swap" rel="stylesheet">
<style>
  :root {
    --cyan: #12b6d8;
    --green: #9bc93b;
    --orange: #f07224;
    --pink: #e2449a;
    --ink: #1c1c1c;
    --paper: #ffffff;
    --sky-top: #ffffff;
    --sky-mid: #8fdaf4;
    --sky-low: #22a9e6;
    --sky-deep: #1a98dd;
  }
  * { box-sizing: border-box; margin: 0; padding: 0; }
  html, body { width: 848px; height: 1200px; overflow: hidden; }
  body {
    font-family: "Quicksand", sans-serif;
    color: var(--ink);
    background: var(--paper);
  }
  .sheet {
    position: relative;
    width: 848px;
    height: 1200px;
    background: linear-gradient(180deg, var(--sky-top) 0%, var(--sky-top) 14%, var(--sky-mid) 34%, var(--sky-low) 55%, var(--sky-deep) 100%);
    overflow: hidden;
  }
  .brand {
    position: absolute; top: 78px; left: 0; width: 848px;
    display: flex; justify-content: center; align-items: center; gap: 14px;
  }
  .brand-dot { width: 34px; height: 34px; border-radius: 50%; background: var(--cyan); }
  .brand-name { font-size: 44px; font-weight: 600; color: #2a2a2a; letter-spacing: 0.5px; }

  .field { position: absolute; top: 186px; display: flex; align-items: flex-end; font-size: 20px; font-weight: 600; }
  .field-line { border-bottom: 1.5px solid var(--ink); margin-left: 6px; height: 20px; }
  .field--name { left: 97px; } .field--name .field-line { width: 234px; }
  .field--date { left: 455px; } .field--date .field-line { width: 244px; }

  .card {
    position: absolute; background: var(--paper);
    border: 1.5px solid var(--accent); border-bottom: 10px solid var(--accent);
    border-radius: 10px;
  }
  .card-tab {
    position: absolute; left: 27px; top: -19px; width: 239px; height: 40px;
    background: var(--accent); border-radius: 8px; color: #fff;
    font-size: 18px; font-weight: 600; text-align: center; line-height: 40px;
  }
  .card--wide .card-tab { left: 202px; top: -15px; height: 29px; line-height: 29px; font-size: 17px; font-weight: 500; }

  .card--nap { left: 97px; top: 250px; width: 296px; height: 198px; --accent: var(--cyan); }
  .card--feed { left: 455px; top: 250px; width: 296px; height: 198px; --accent: var(--green); }
  .card--diapers { left: 97px; top: 485px; width: 296px; height: 198px; --accent: var(--orange); }
  .card--mood { left: 455px; top: 485px; width: 296px; height: 198px; --accent: var(--pink); }
  .card--activities { left: 97px; top: 716px; width: 654px; height: 111px; --accent: var(--pink); }
  .card--supplies { left: 97px; top: 851px; width: 654px; height: 112px; --accent: var(--orange); }
  .card--notes { left: 97px; top: 987px; width: 654px; height: 112px; --accent: var(--green); }

  .col-head { position: absolute; top: 36px; font-size: 18px; }
  .log-line { position: absolute; height: 0; border-top: 1.5px solid var(--ink); }
  .log-line--short { left: 27px; width: 53px; }
  .log-line--long { left: 123px; width: 140px; }

  .box { position: absolute; width: 18px; height: 18px; border: 1.5px solid #333; background: #fff; }
  .box--sm { width: 13px; height: 13px; border-width: 1.2px; }

  .mood-item { position: absolute; font-size: 18px; line-height: 20px; }
  .mood-item .box { width: 14px; height: 14px; left: -27px; top: 3px; }

  .supply { position: absolute; font-size: 13px; line-height: 16px; }
  .supply .box { left: -24px; top: 1px; }

  .note-line { position: absolute; left: 26px; width: 597px; border-top: 1.3px solid var(--ink); }

  .footer {
    position: absolute; left: 0; top: 1120px; width: 848px; height: 41px;
    background: var(--orange); color: #fff; text-align: center;
    font-size: 19px; font-weight: 500; letter-spacing: 3px; line-height: 41px;
  }
</style>
</head>
<body>
<main class="sheet">
  <header class="brand">
    <span class="brand-dot"></span>
    <span class="brand-name">Plum Hollow Kit</span>
  </header>

  <div class="field field--name">Name <span class="field-line"></span></div>
  <div class="field field--date">Date <span class="field-line"></span></div>

  <section class="card card--nap">
    <h2 class="card-tab">NAP TIME</h2>
    <span class="col-head" style="left:27px">Time</span>
    <span class="col-head" style="left:155px">How Long</span>
    <span class="log-line log-line--short" style="top:85px"></span><span class="log-line log-line--long" style="top:85px"></span>
    <span class="log-line log-line--short" style="top:115px"></span><span class="log-line log-line--long" style="top:115px"></span>
    <span class="log-line log-line--short" style="top:145px"></span><span class="log-line log-line--long" style="top:145px"></span>
    <span class="log-line log-line--short" style="top:175px"></span><span class="log-line log-line--long" style="top:175px"></span>
  </section>

  <section class="card card--feed">
    <h2 class="card-tab">FEEDING</h2>
    <span class="col-head" style="left:27px">Time</span>
    <span class="col-head" style="left:166px">What</span>
    <span class="log-line log-line--short" style="top:85px"></span><span class="log-line log-line--long" style="top:85px"></span>
    <span class="log-line log-line--short" style="top:115px"></span><span class="log-line log-line--long" style="top:115px"></span>
    <span class="log-line log-line--short" style="top:145px"></span><span class="log-line log-line--long" style="top:145px"></span>
    <span class="log-line log-line--short" style="top:175px"></span><span class="log-line log-line--long" style="top:175px"></span>
  </section>

  <section class="card card--diapers">
    <h2 class="card-tab">DIAPERS</h2>
    <span class="col-head" style="left:27px">Time</span>
    <span class="col-head" style="left:142px">Wet</span>
    <span class="col-head" style="left:218px">BM</span>
    <span class="log-line log-line--short" style="top:85px"></span><span class="box" style="left:148px;top:66px"></span><span class="box" style="left:220px;top:66px"></span>
    <span class="log-line log-line--short" style="top:115px"></span><span class="box" style="left:148px;top:96px"></span><span class="box" style="left:220px;top:96px"></span>
    <span class="log-line log-line--short" style="top:144px"></span><span class="box" style="left:148px;top:125px"></span><span class="box" style="left:220px;top:125px"></span>
    <span class="log-line log-line--short" style="top:174px"></span><span class="box" style="left:148px;top:155px"></span><span class="box" style="left:220px;top:155px"></span>
  </section>

  <section class="card card--mood">
    <h2 class="card-tab">MOOD</h2>
    <span class="mood-item" style="left:54px;top:36px"><span class="box"></span>Happy</span>
    <span class="mood-item" style="left:54px;top:66px"><span class="box"></span>Sad</span>
    <span class="mood-item" style="left:54px;top:95px"><span class="box"></span>Unsettled</span>
    <span class="mood-item" style="left:54px;top:125px"><span class="box"></span>Energetic</span>
    <span class="mood-item" style="left:54px;top:154px"><span class="box"></span>Tired</span>
    <span class="mood-item" style="left:196px;top:36px"><span class="box"></span>Chatty</span>
    <span class="mood-item" style="left:196px;top:66px"><span class="box"></span>Quiet</span>
  </section>

  <section class="card card--wide card--activities">
    <h2 class="card-tab">Today's Activities</h2>
  </section>

  <section class="card card--wide card--supplies">
    <h2 class="card-tab">Supplies Needed Soon</h2>
    <span class="supply" style="left:75px;top:36px"><span class="box box--sm"></span>Diapers</span>
    <span class="supply" style="left:75px;top:56px"><span class="box box--sm"></span>Diaper Cream</span>
    <span class="supply" style="left:75px;top:76px"><span class="box box--sm"></span>Other:</span>
    <span class="supply" style="left:270px;top:36px"><span class="box box--sm"></span>Milk/Formula</span>
    <span class="supply" style="left:270px;top:56px"><span class="box box--sm"></span>Cereal</span>
    <span class="supply" style="left:504px;top:36px"><span class="box box--sm"></span>Wet Wipes</span>
    <span class="supply" style="left:504px;top:56px"><span class="box box--sm"></span>Baby Food</span>
  </section>

  <section class="card card--wide card--notes">
    <h2 class="card-tab">Special Notes</h2>
    <span class="note-line" style="top:45px"></span>
    <span class="note-line" style="top:66px"></span>
    <span class="note-line" style="top:87px"></span>
  </section>

  <footer class="footer">www.plumhollowkit.com</footer>
</main>
</body>
</html>
```